Design and Renovation Company Luxury Business Card

I want to create a luxury business card for a Design and Renovation Firm . We will use our current logo. The company name is 742BUILD. We do not want anything standard. We need a very unique concept.
Please see uploaded inspiration. I really like the textured paper option. I would like the card to be thick with debossing, and/or embossing options. The logo has orange in it but I would like to see the card with and without the orange. I think the orange may make the company feel less high-end. The goal is to elevate the logo not match its vibe per se of the logo. We want something very unique, not standard at all!
I would like a space for :
Logo,
Name,
Position,
Email,
Office number,
Website Address,
Business Address,
Thank you!
Have fun!
Target Market(s)
Home owners Age 35 +
Industry/Entity Type
Design and Renovation
Contact Information for Business Card
Logo, Name, Position, Email, Office number, Website Address, Business Address,.
Colors
Designer to choose colors to be used in the design.
Requirements
Must have
- A luxury designer feel. Must be black or dark grey but open to other luxury ideas.
Nice to have
- Gold, silver, black embossing or debossing. Textured paper design.
Should not have
- A cheap look and feel.

```html
<!DOCTYPE html>
<html lang="en">
<head>
<meta charset="utf-8">
<title>742BUILD Business Card</title>
<link href="https://fonts.googleapis.com/css2?family=Roboto:wght@400;500&display=swap" rel="stylesheet">
<style>
  :root {
    --page: #161616;
    --card: #2f2f2f;
    --card-deep: #262626;
    --ink: #f2f2f2;
    --ink-soft: #cfcfcf;
    --accent: #e8921f;
    --divider: #8a8a8a;
  }
  * { margin: 0; padding: 0; box-sizing: border-box; }
  html, body {
    width: 1200px; height: 840px; overflow: hidden;
    background: var(--page);
    font-family: "Roboto", sans-serif;
  }
  .canvas {
    width: 1200px; height: 840px;
    display: flex; align-items: center; justify-content: center; gap: 50px;
  }
  .card {
    position: relative;
    width: 540px; height: 310px;
    border-radius: 22px;
    background: linear-gradient(160deg, var(--card) 0%, var(--card-deep) 100%);
    border-bottom: 4px solid var(--accent);
    border-left: 2px solid var(--accent);
    overflow: hidden;
  }

  .company-name {
    font-weight: 500; color: var(--ink); line-height: 1; letter-spacing: 2px;
  }
  .company-line {
    font-weight: 400; color: var(--ink-soft); line-height: 1.2;
  }

  /* Brand side */
  .brand-side .company-block { position: absolute; left: 36px; top: 60px; }
  .brand-side .company-name { font-size: 50px; }
  .brand-side .company-line { font-size: 12px; margin-top: 8px; }
  .tile-grid { position: absolute; right: 0; top: 0; width: 270px; height: 310px; }

  /* Contact side */
  .contact-side .company-block {
    position: absolute; left: 0; right: 0; top: 52px; text-align: center;
  }
  .contact-side .company-name { font-size: 46px; }
  .contact-side .company-line { font-size: 12px; margin-top: 8px; }

  .details {
    position: absolute; left: 0; right: 0; top: 160px;
    display: flex; align-items: center; justify-content: center;
  }
  .person { text-align: right; padding-right: 18px; }
  .person-name {
    font-weight: 500; font-size: 20px; color: var(--accent);
    text-transform: uppercase;
  }
  .person-role { font-size: 15px; color: var(--ink); margin-top: 2px; }
  .rule { width: 1px; height: 70px; background: var(--divider); }
  .contacts { list-style: none; padding-left: 16px; }
  .contacts li {
    display: flex; align-items: center; gap: 8px;
    font-size: 15px; color: var(--ink); line-height: 23px;
  }
  .contacts svg { width: 13px; height: 13px; flex: none; }
  .address {
    position: absolute; left: 0; right: 0; bottom: 30px;
    text-align: center; font-size: 15px; color: var(--ink);
  }
</style>
</head>
<body>
<main class="canvas">

  <section class="card brand-side" aria-label="Card back">
    <div class="company-block">
      <div class="company-name">742BUILD</div>
      <div class="company-line">Design and Renovation Firm</div>
    </div>
    <svg class="tile-grid" viewBox="0 0 270 310" aria-hidden="true">
      <defs>
        <linearGradient id="panelSheen" x1="0" y1="0" x2="1" y2="1">
          <stop offset="0" stop-color="#1f1f1f"/>
          <stop offset="0.55" stop-color="#3a3a3a"/>
          <stop offset="1" stop-color="#8a8a8a"/>
        </linearGradient>
        <linearGradient id="panelSheenLight" x1="0" y1="0" x2="1" y2="1">
          <stop offset="0" stop-color="#4a4a4a"/>
          <stop offset="1" stop-color="#9a9a9a"/>
        </linearGradient>
      </defs>
      <rect x="110" y="0" width="160" height="120" fill="url(#panelSheen)"/>
      <rect x="20" y="150" width="140" height="160" fill="url(#panelSheen)"/>
      <rect x="180" y="150" width="90" height="160" fill="url(#panelSheenLight)"/>
    </svg>
  </section>

  <section class="card contact-side" aria-label="Card front">
    <div class="company-block">
      <div class="company-name">742BUILD</div>
      <div class="company-line">Design and Renovation Firm</div>
    </div>

    <div class="details">
      <div class="person">
        <div class="person-name">Marcus Hale</div>
        <div class="person-role">Manager</div>
      </div>
      <div class="rule"></div>
      <ul class="contacts">
        <li>
          <svg viewBox="0 0 16 16" aria-hidden="true"><path fill="#e8921f" d="M3 1.5h3l1.2 3.2-1.8 1.2a9 9 0 0 0 4.7 4.7l1.2-1.8 3.2 1.2v3a1.5 1.5 0 0 1-1.6 1.5A13 13 0 0 1 1.5 3.1 1.5 1.5 0 0 1 3 1.5z"/></svg>
          555-314-2700
        </li>
        <li>
          <svg viewBox="0 0 16 16" aria-hidden="true"><rect x="1" y="3" width="14" height="10" rx="1" fill="#e8921f"/><path d="M1.5 3.8 8 9l6.5-5.2" fill="none" stroke="#2f2f2f" stroke-width="1.3"/></svg>
          hello@742build.com
        </li>
        <li>
          <svg viewBox="0 0 16 16" aria-hidden="true"><circle cx="8" cy="8" r="7" fill="#e8921f"/><path d="M1 8h14M8 1c-2.6 2.2-2.6 11.8 0 14M8 1c2.6 2.2 2.6 11.8 0 14" fill="none" stroke="#2f2f2f" stroke-width="1.1"/></svg>
          www.742build.com
        </li>
      </ul>
    </div>

    <p class="address">Your Address, City, State, Zip 0000</p>
  </section>

</main>
</body>
</html>
```